Harborstone Lending Business Card Design

We are looking for a nice looking business card design. I'd prefer something other than white for the background but white is ok if necessary. I'm uploading two versions of my picture, one is square and one is rounded. Also a couple of versions of the logo for white backgrounds as well as one for darker backgrounds.

Target Market(s)

Realtors and prospective clients

Industry/Entity Type

Mortgage

Contact Information for Business Card

Double sided business card. Not sure what is needed here.

Colors

Designer to choose colors to be used in the design.

Requirements
Must have
• Name: Marcus Pellham
• Title: Senior Mortgage Advisor
• Email: marcuspellham@harborstonelending.example
• website: www.marcuspellhamhomeloangroup.example
• Address: 4670 W 2850 N, STE 215 Salt Lake City, UT 84192
• Phone: 801-555-0187
• nmls# 948217
• Logo is on our webstie. www.harborstonelending.example
• Picture
Nice to have
• Colors could be similar to our website www.harborstonelending.example
• A list of what we do (VA Loans, FHA Loans, Conventional Loans, USDA Loans)

```html
<!DOCTYPE html>
<html lang="en">
<head>
<meta charset="utf-8">
<title>Harborstone Lending Business Card</title>
<link rel="stylesheet" href="https://fonts.googleapis.com/css2?family=Jost:wght@400;600&family=Source+Sans+3:wght@400;600&display=swap">
<style>
  :root {
    --backdrop: #c49a6e;
    --card-white: #ffffff;
    --ink: #1b1b1b;
    --black: #060606;
    --charcoal: #1e1f21;
    --slate: #4a4b4d;
    --silver: #b9babc;
    --pale-grey: #d6d6d6;
    --accent-green: #5ea53c;
    --text-light: #f2f2f2;
    --text-muted: #c9c9c9;
  }
  * { margin: 0; padding: 0; box-sizing: border-box; }
  html, body { width: 1200px; height: 480px; overflow: hidden; }
  body {
    background: var(--backdrop);
    position: relative;
    font-family: "Source Sans 3", Arial, sans-serif;
  }
  .card {
    position: absolute;
    width: 475px;
    height: 272px;
    overflow: hidden;
    box-shadow: 3px 4px 6px rgba(0,0,0,0.35);
  }
  .card-front { left: 86px; top: 93px; background: var(--card-white); }
  .card-back { left: 591px; top: 91px; background: var(--black); }
  .card-shapes { position: absolute; inset: 0; width: 100%; height: 100%; }

  .brand-name {
    position: absolute;
    font-family: "Jost", Arial, sans-serif;
    font-weight: 600;
    letter-spacing: 2.5px;
    text-transform: uppercase;
    white-space: nowrap;
  }
  .card-front .brand-name { left: 22px; top: 36px; font-size: 22px; color: var(--ink); }
  .card-back .brand-name { left: 25px; top: 118px; font-size: 17px; line-height: 1.25; color: var(--silver); }

  .person-name {
    position: absolute; left: 30px; top: 92px;
    font-family: "Jost", Arial, sans-serif;
    font-size: 18px; font-weight: 400;
    color: var(--accent-green);
  }
  .person-title {
    position: absolute; left: 30px; top: 117px;
    font-family: "Jost", Arial, sans-serif;
    font-size: 11px; color: var(--ink);
  }
  .portrait {
    position: absolute; left: 339px; top: 30px;
    width: 116px; height: 116px; border-radius: 50%;
    border: 2px solid #8d8d8d;
    background: radial-gradient(circle at 50% 45%, #c79a7e 0%, #8a6650 38%, #6b5a3c 62%, #3d3f3a 100%);
  }
  .contact {
    position: absolute; right: 27px; top: 173px;
    text-align: right; color: var(--text-light);
    font-size: 12px; line-height: 17px;
  }
  .contact .label { font-weight: 600; }
  .contact .value-muted { color: var(--text-muted); }
  .contact .address { margin-top: 15px; }

  .license {
    position: absolute; right: 26px; top: 29px;
    font-size: 12px; color: var(--text-muted); letter-spacing: 0.3px;
  }
  .services {
    position: absolute; right: 22px; top: 170px;
    list-style: none; text-align: right;
    color: var(--text-light); font-size: 13px; line-height: 20.5px;
  }
  .services li { display: flex; justify-content: flex-end; align-items: center; gap: 8px; }
  .services svg { width: 11px; height: 11px; }
</style>
</head>
<body>

  <section class="card card-front">
    <svg class="card-shapes" viewBox="0 0 475 272" preserveAspectRatio="none" aria-hidden="true">
      <polygon points="0,212 0,272 128,272" fill="var(--pale-grey)"/>
      <polygon points="0,212 128,272 200,272 60,236" fill="#a9a9a9"/>
      <polygon points="128,272 475,90 475,272" fill="var(--black)"/>
      <polygon points="60,236 475,88 475,92 128,272 118,268" fill="var(--silver)" opacity="0.8"/>
    </svg>
    <div class="brand-name">Harborstone Lending</div>
    <div class="person-name">Marcus Pellham</div>
    <div class="person-title">Senior Mortgage Advisor</div>
    <div class="portrait" role="img" aria-label="Portrait photo of Marcus Pellham"></div>
    <div class="contact">
      <div><span class="label">Phone:</span> <span class="value-muted">801-555-0187</span></div>
      <div>marcuspellham@harborstonelending.example</div>
      <div>www.marcuspellhamhomeloangroup.example</div>
      <div class="address">4670 W 2850 N, STE 215 Salt Lake City, UT 84192</div>
    </div>
  </section>

  <section class="card card-back">
    <svg class="card-shapes" viewBox="0 0 475 272" preserveAspectRatio="none" aria-hidden="true">
      <polygon points="0,209 475,86 475,272 0,272" fill="var(--charcoal)"/>
      <polygon points="0,209 0,272 128,272" fill="var(--slate)"/>
      <polygon points="0,209 128,272 170,272" fill="#333436"/>
    </svg>
    <div class="license">nmls# 948217</div>
    <div class="brand-name">Harborstone<br>Lending</div>
    <ul class="services">
      <li>VA Loans <svg viewBox="0 0 10 10"><path d="M5 0 L6.2 3.8 L10 5 L6.2 6.2 L5 10 L3.8 6.2 L0 5 L3.8 3.8 Z" fill="var(--accent-green)"/></svg></li>
      <li>FHA Loans <svg viewBox="0 0 10 10"><path d="M5 0 L6.2 3.8 L10 5 L6.2 6.2 L5 10 L3.8 6.2 L0 5 L3.8 3.8 Z" fill="var(--accent-green)"/></svg></li>
      <li>Conventional Loans <svg viewBox="0 0 10 10"><path d="M5 0 L6.2 3.8 L10 5 L6.2 6.2 L5 10 L3.8 6.2 L0 5 L3.8 3.8 Z" fill="var(--accent-green)"/></svg></li>
      <li>USDA Loans <svg viewBox="0 0 10 10"><path d="M5 0 L6.2 3.8 L10 5 L6.2 6.2 L5 10 L3.8 6.2 L0 5 L3.8 3.8 Z" fill="var(--accent-green)"/></svg></li>
    </ul>
  </section>

</body>
</html>
```